Vantage Sport And Fitness- Rates

I am opening up a new Gym/Training Facility. The Name of my New gym is Vantage Sports And Fitness. I am wanting to design a card that captures Membership Pricing/Personal Training Pricing. I will Upload the Logo. My colors are Red/Black/Silver. I really want there pricing card to "POP". IT needs to be very Professional and Clean. I will be placing these cards on a 5'7 . I would like these item on the card:
Name of Company: Vantage Sports And Fitness
Address:
2817 Larkmoor Commerce Dr.
Suite 214 Chantilly, VA 20153
Phone #: 703-555-0187
website: www.vantagesnf-example.com
Membership Rates:
$99/Month
$49 Heroes Rate
Family Plan:
2 People $149
3 People $199
4 People $299
Personal Training Rates:
1 session $102
5 sessions $490
10 sessions $940
20 sessions $1,800
40 sessions $3,400
Please be creative

```html
<!DOCTYPE html>
<html lang="en">
<head>
<meta charset="utf-8">
<title>Vantage Sports And Fitness – Rates Card</title>
<link rel="stylesheet" href="https://fonts.googleapis.com/css2?family=Montserrat:wght@400;600;700&family=Quicksand:wght@400;500&family=PT+Sans:wght@400;700&display=swap">
<style>
  :root {
    --red: #e41e26;
    --red-deep: #c3141b;
    --black: #0b0b0b;
    --silver: #6a6a6a;
    --silver-dark: #3d3d3d;
    --white: #ffffff;
    --stage: #3a3a3a;
  }
  html, body {
    margin: 0;
    width: 1200px;
    height: 1200px;
    overflow: hidden;
    background: var(--stage);
  }
  .rates-card {
    position: absolute;
    left: 241px;
    top: 30px;
    width: 718px;
    height: 1140px;
    display: block;
  }
  .brand-name { font-family: "Montserrat", sans-serif; font-weight: 600; font-size: 20px; fill: var(--white); }
  .connect-label { font-family: "Montserrat", sans-serif; font-weight: 600; font-size: 14px; fill: var(--red); }
  .headline { font-family: "Montserrat", sans-serif; font-weight: 700; fill: var(--white); }
  .subline { font-family: "Quicksand", sans-serif; font-weight: 400; fill: var(--white); }
  .badge-price { font-family: "Montserrat", sans-serif; font-weight: 600; fill: var(--red); }
  .badge-text { font-family: "Montserrat", sans-serif; font-weight: 600; fill: var(--white); }
  .badge-accent { fill: var(--red); }
  .section-title { font-family: "Montserrat", sans-serif; font-weight: 600; font-size: 22px; fill: var(--white); letter-spacing: -0.5px; }
  .price-line { font-family: "PT Sans", sans-serif; font-weight: 400; font-size: 22px; fill: var(--white); }
  .rate-bubble-text { font-family: "PT Sans", sans-serif; font-weight: 400; fill: var(--white); }
  .contact { font-family: "PT Sans", sans-serif; font-size: 16px; fill: var(--white); }
  .address { font-family: "PT Sans", sans-serif; font-size: 14px; fill: var(--white); }
</style>
</head>
<body>
<svg class="rates-card" viewBox="0 0 718 1140" xmlns="http://www.w3.org/2000/svg">
  <defs>
    <radialGradient id="heroGlow" cx="0.5" cy="0.35" r="0.6">
      <stop offset="0" stop-color="#4d6068"/>
      <stop offset="0.55" stop-color="#1c2428"/>
      <stop offset="1" stop-color="#0b0b0b"/>
    </radialGradient>
    <linearGradient id="silverPanel" x1="0" y1="0" x2="1" y2="0">
      <stop offset="0" stop-color="#3b3b3b"/>
      <stop offset="0.4" stop-color="#6e6e6e"/>
      <stop offset="0.7" stop-color="#575757"/>
      <stop offset="1" stop-color="#3a3a3a"/>
    </linearGradient>
    <linearGradient id="redBand" x1="0" y1="0" x2="1" y2="1">
      <stop offset="0" stop-color="#f0242c"/>
      <stop offset="1" stop-color="#c0121a"/>
    </linearGradient>
    <radialGradient id="badgeFill" cx="0.4" cy="0.35" r="0.7">
      <stop offset="0" stop-color="#6b6b6b"/>
      <stop offset="1" stop-color="#2a2a2a"/>
    </radialGradient>
    <radialGradient id="bubbleFill" cx="0.4" cy="0.3" r="0.7">
      <stop offset="0" stop-color="#f3323a"/>
      <stop offset="1" stop-color="#c8141c"/>
    </radialGradient>
  </defs>

  <rect class="card-base" width="718" height="1140" fill="var(--black)"/>

  <rect class="hero-photo" x="0" y="95" width="718" height="480" fill="url(#heroGlow)"
        role="img" aria-label="Photo of a man and a woman lifting dumbbells back to back"/>

  <rect class="pricing-panel" x="0" y="560" width="718" height="580" fill="url(#silverPanel)"/>

  <path class="promo-band" fill="url(#redBand)"
        d="M0 548 L40 530 L60 536 L110 520 L200 505 L250 485 L270 490 L330 470 L380 450 L420 440 L470 420 L520 410 L560 395 L600 390 L640 380 L680 372 L700 360 L718 355
           L718 612 L690 622 L640 632 L600 650 L560 655 L520 670 L470 690 L440 695 L380 718 L350 724 L300 745 L270 742 L220 762 L180 770 L150 780 L120 790 L90 782 L60 800 L30 805 L0 812 Z"/>

  <!-- brand header -->
  <circle class="brand-dot" cx="52" cy="70" r="14" fill="var(--red)"/>
  <text class="brand-name" x="76" y="77">Vantage Sports And Fitness</text>

  <text class="connect-label" x="426" y="76">LET'S STAY CONNECTED</text>
  <circle class="social-dot" cx="638" cy="71" r="12" fill="var(--white)"/>
  <circle class="social-dot" cx="671" cy="71" r="12" fill="var(--white)"/>

  <!-- enrollment badge -->
  <ellipse cx="150" cy="712" rx="95" ry="8" fill="#000" opacity="0.35"/>
  <circle class="offer-badge-ring" cx="147" cy="601" r="114" fill="var(--white)"/>
  <circle class="offer-badge" cx="147" cy="601" r="106" fill="var(--red-deep)"/>
  <circle class="offer-badge" cx="147" cy="601" r="99" fill="url(#badgeFill)"/>
  <text class="badge-price" x="147" y="572" font-size="44" text-anchor="middle">$49</text>
  <text class="badge-text" x="147" y="608" font-size="18" text-anchor="middle">ENROLLMENT</text>
  <text class="badge-text" x="147" y="634" font-size="18" text-anchor="middle">AND GET A <tspan class="badge-accent">FREE</tspan></text>
  <text class="badge-text" x="147" y="659" font-size="18" text-anchor="middle">PT SESSION!</text>

  <!-- headline -->
  <g class="headline-group" transform="rotate(-17 470 560)">
    <text class="headline" x="270" y="555" font-size="46">JOIN US TODAY</text>
    <text class="subline" x="322" y="595" font-size="30">Membership Pricing/</text>
    <text class="subline" x="282" y="632" font-size="30">Personal Training Pricing.</text>
  </g>

  <!-- family plan -->
  <text class="section-title" x="318" y="801">FAMILY PLAN:</text>
  <text class="price-line" x="318" y="838">2 People $149 | 3 People $199</text>
  <text class="price-line" x="318" y="865">4 People $299</text>

  <!-- membership rates -->
  <text class="section-title" x="44" y="926">MEMBERSHIP RATES:</text>
  <circle class="rate-bubble" cx="98" cy="1000" r="53" fill="url(#bubbleFill)"/>
  <text class="rate-bubble-text" x="98" y="993" font-size="26" text-anchor="middle">$99/</text>
  <text class="rate-bubble-text" x="98" y="1021" font-size="26" text-anchor="middle">Month</text>
  <circle class="rate-bubble" cx="223" cy="1000" r="53" fill="url(#bubbleFill)"/>
  <text class="rate-bubble-text" x="223" y="982" font-size="24" text-anchor="middle">$49</text>
  <text class="rate-bubble-text" x="223" y="1007" font-size="24" text-anchor="middle">Heroes</text>
  <text class="rate-bubble-text" x="223" y="1032" font-size="24" text-anchor="middle">Rate</text>

  <!-- personal training rates -->
  <text class="section-title" x="318" y="926">PERSONAL TRAINING RATES:</text>
  <text class="price-line" x="318" y="966">1 session $102 | 5 sessions $490</text>
  <text class="price-line" x="318" y="993">10 sessions $940 | 20 sessions $1,800</text>
  <text class="price-line" x="318" y="1020">40 sessions $3,400</text>

  <!-- footer -->
  <path class="footer-band" fill="var(--red)" d="M0 1098 L400 1098 L718 1020 L718 1140 L0 1140 Z"/>
  <path class="icon-pin" fill="var(--white)"
        d="M593 1070 a6 6 0 0 1 6 6 c0 5 -6 11 -6 11 s-6 -6 -6 -11 a6 6 0 0 1 6 -6 z M593 1073.5 a2.5 2.5 0 1 0 0.01 0 z"/>
  <text class="address" x="690" y="1099" text-anchor="end">2817 Larkmoor Commerce Dr.</text>
  <text class="address" x="690" y="1118" text-anchor="end">Suite 214 Chantilly, VA 20153</text>

  <path class="icon-phone" fill="var(--white)"
        d="M41 1110 h9 l2 3 h-3 v3 h-7 v-3 h-3 z"/>
  <text class="contact" x="58" y="1125">703-555-0187</text>
  <circle class="icon-web" cx="203" cy="1119" r="5" fill="none" stroke="var(--white)" stroke-width="1.5"/>
  <line x1="198" y1="1119" x2="208" y2="1119" stroke="var(--white)" stroke-width="1"/>
  <text class="contact" x="214" y="1124">www.vantagesnf-example.com</text>
</svg>
</body>
</html>
```